Feminine colorfull packaging for coconut skin care brand

We need a design that can be used on different types of packaging for beauty products likes creams, oils, etc.
The products that we will launch will be made with one key ingredient of coconut oil + other added ingredients depending on the type of product. The entire marketing will therefore be based on COCONUTS, palmtrees, sand, beach, bronzing on the beach, holiday feeling, nature, femininity, etc. = A Lifestyle brand with a tropical vibe.
Packaging can be a pot for creams, flaskes for lotions, smaller bottles for oils, etc. Mostly the standard packaging used for beauty products.
We would like to use the color pink ( this can be bright or pastel or any tone of pink) to address the feminine side of our product and a tone of blue-green ( pastel, bright or any tone of this color) to accentuate the use of coconut.
Third would be the color white (this can be added through an accent somewhere on the packaging or this can be the brand name that is written in white)
Lastely we would like the packaging to be light, fresh and playfull. Please feel free to use different colors or shapes ( we do not yet have a logo. This can then be designed followed on the packaging)
The design will be printed on plastic packaging. We are open to very creative designs. We are looking for packaging that catches the eye by its design and/or colors, that is different than others, that distinguishes the product because of its packaging design.
Target Market(s)
Women between 20 - 35 years
Industry/Entity Type
Beauty
Colors
Designer to choose colors to be used in the design.
Look and feel

```html
<!DOCTYPE html>
<html lang="en">
<head>
<meta charset="utf-8">
<title>Palmera Nourishing Body Milk – Label</title>
<link rel="stylesheet" href="https://fonts.googleapis.com/css2?family=Courgette&display=swap">
<style>
  :root {
    --label-pink: #f1b4d3;
    --leaf-pink: #ec8db1;
    --brand-ink: #111111;
    --product-ink: #c4234f;
    --page: #ffffff;
  }
  html, body {
    margin: 0;
    padding: 0;
    width: 886px;
    height: 1200px;
    overflow: hidden;
    background: var(--page);
  }
  .label {
    position: relative;
    width: 886px;
    height: 1200px;
    background: var(--label-pink);
    overflow: hidden;
  }
  .palm-frond {
    position: absolute;
    left: 0;
    top: 300px;
    width: 886px;
    height: 520px;
  }
  .brand-name {
    position: absolute;
    left: 0;
    right: 0;
    top: 360px;
    margin: 0;
    text-align: center;
    font-family: "Courgette", cursive;
    font-weight: 400;
    font-size: 150px;
    line-height: 1;
    color: var(--brand-ink);
  }
  .product-name {
    position: absolute;
    left: 0;
    right: 0;
    top: 800px;
    margin: 0;
    text-align: center;
    font-family: "Courgette", cursive;
    font-weight: 400;
    font-size: 92px;
    line-height: 1.3;
    color: var(--product-ink);
  }
</style>
</head>
<body>
  <main class="label">
    <svg class="palm-frond" viewBox="0 0 886 520" role="img" aria-label="Pink palm frond illustration sweeping across the label">
      <defs>
        <linearGradient id="frond-tone" x1="0" y1="1" x2="1" y2="0">
          <stop offset="0" stop-color="var(--leaf-pink)" stop-opacity="0.55"/>
          <stop offset="1" stop-color="var(--leaf-pink)" stop-opacity="0.9"/>
        </linearGradient>
      </defs>
      <ellipse cx="500" cy="260" rx="460" ry="150" transform="rotate(-28 500 260)" fill="url(#frond-tone)"/>
    </svg>

    <h1 class="brand-name">Palmera</h1>

    <p class="product-name">Nourishing<br>Body Milk</p>
  </main>
</body>
</html>
```